Job site for brightlarkyard.com

Update: Looking for a really simple design that is fit for a short attention span.
Need a website built that I can host on Zentrovo.com.
Need tracking: Important to track where students are clicking and be able to provide that detail to employers.
The site will use the brightlarkyard.com logo (attached).
Add a tagline - Highschool Students Start Here
( Link on main page) Job Opportunities (click to page)
- Listing of new jobs.
o Job Title
o Company Name
o Position Description
o Hyperlink to employer website (need to be able to track clicks)
(Link on main page) Tools & Career Advice (click to page)
o This section would allow for the posting of advice and articles.
(Link on main page) Ask a Job Question? (click to page)
o Submit a question via email – email only collected. No personal
info.
(Link on main page) Volunteer Opportunities (click to page)
o A listing of organizations that need student volunteers. Need
to be able to add a new listing. Similar to a job listing:
Business or Non-profit Name
Description of need
Hyperlink to website or simply contact info.
(Link on main page) About Us
- Be able to change the content
Updates
Gathering more feedback
Target Market(s)
Ages 14-18
Industry/Entity Type
job board
Coding
Coded - Design and coding required
Number of Pages Required
4 page

```html
<!DOCTYPE html>
<html lang="en">
<head>
<meta charset="utf-8">
<title>brightlarkyard.com — Highschool Students Start Here</title>
<link rel="stylesheet" href="https://fonts.googleapis.com/css2?family=Roboto:wght@400;500;700;900&family=Arimo:wght@400;700&display=swap">
<style>
:root{
  --cyan:#22b6df;
  --cyan-dark:#1aa3c9;
  --ink:#222a31;
  --text:#3a3f44;
  --muted:#7a7f84;
  --slate:#2e3b47;
  --footer:#35414c;
  --line:#d9dde0;
  --white:#ffffff;
}
*{box-sizing:border-box;margin:0;padding:0}
html,body{width:1200px;height:3954px;overflow:hidden;background:var(--white)}
body{position:relative;font-family:"Arimo",Arial,sans-serif;color:var(--text)}
.abs{position:absolute}
h2.section-title{position:absolute;left:0;width:1200px;text-align:center;font-family:"Roboto",Arial,sans-serif;font-weight:500;font-size:34px;color:var(--ink);letter-spacing:.3px}

/* nav */
.topline{top:0;left:0;width:1200px;height:3px;background:var(--cyan)}
.nav-pointer{top:3px;left:146px}
.main-nav{top:0;left:0;width:1200px;height:72px;display:flex;justify-content:center;align-items:center;gap:0;font-family:"Roboto",Arial,sans-serif;font-size:14px;font-weight:500;color:#333;text-transform:uppercase}
.main-nav a{color:#333;text-decoration:none;padding:0 14px;border-left:1px solid #c9cdd1;line-height:16px}
.main-nav a:first-child{border-left:none}

/* hero */
.hero{top:72px;left:0;width:1200px;height:625px;background:linear-gradient(100deg,#8c9a6a 0%,#c7b79e 30%,#e8dcd0 50%,#b9b6ad 72%,#6f7d66 100%)}
.hero-shade{top:72px;left:0;width:1200px;height:625px;background:linear-gradient(180deg,rgba(0,0,0,0) 30%,rgba(0,0,0,.25) 100%)}
.brand-box{top:72px;left:107px;width:152px;height:134px;background:var(--white);display:flex;align-items:flex-end;justify-content:center;padding-bottom:22px}
.brand-name{font-family:"Arimo",Arial,sans-serif;font-weight:400;font-size:17px;color:var(--cyan-dark)}
.hero-title{top:378px;left:0;width:1200px;text-align:center;font-family:"Roboto",Arial,sans-serif;font-weight:900;font-size:58px;line-height:60px;color:var(--white);text-shadow:0 2px 6px rgba(0,0,0,.45)}
.btn-pill{display:inline-flex;align-items:center;justify-content:center;background:var(--cyan);color:var(--white);font-family:"Roboto",Arial,sans-serif;font-weight:500;text-transform:uppercase;border-radius:24px;text-decoration:none}
.hero-cta{top:514px;left:514px;width:172px;height:45px;font-size:15px}
.hero-dots{top:642px;left:575px;display:flex;gap:5px}
.hero-dots span{width:12px;height:12px;border-radius:50%;background:var(--white)}
.hero-dots span.active{background:var(--cyan)}
.hero-social{top:316px;left:1137px;display:flex;flex-direction:column;gap:10px}
.hero-social span{width:27px;height:27px;border-radius:50%;border:1.5px solid var(--white)}

/* listing cards */
.card-row{left:110px;width:978px;display:flex;justify-content:space-between}
.listing-card{width:314px;border:3px solid #2c3238;background:var(--white);position:relative}
.listing-photo{height:215px}
.listing-body{padding:14px 24px 0 24px}
.listing-title{font-family:"Roboto",Arial,sans-serif;font-weight:500;font-size:21px;color:#2e3338}
.listing-company{margin-top:10px;font-weight:700;font-size:14px;color:var(--cyan)}
.listing-desc{margin-top:10px;font-size:13px;line-height:22px;color:var(--muted)}
.employer-btn{position:absolute;right:0;bottom:0;width:116px;height:43px;background:var(--cyan);color:var(--white);font-family:"Roboto",Arial,sans-serif;font-weight:700;font-size:14px;display:flex;align-items:center;justify-content:center;text-decoration:none}
.contact-btn{display:inline-flex;margin-top:14px;width:116px;height:42px;background:var(--cyan);color:var(--white);font-family:"Roboto",Arial,sans-serif;font-weight:700;font-size:14px;align-items:center;justify-content:center;text-decoration:none}

/* about */
.about-band{top:1407px;left:0;width:1200px;height:536px;background:linear-gradient(90deg,#34424e 0%,#3c4a56 40%,#2b3843 100%)}
.about-art{top:1468px;left:166px;width:363px;height:413px;border-radius:48% 48% 46% 46%;background:radial-gradient(circle at 50% 45%,#e7e1da 0%,#bfb7ae 45%,#8f8a85 100%)}
.about-title{top:1478px;left:598px;font-family:"Roboto",Arial,sans-serif;font-weight:500;font-size:36px;color:var(--white)}
.about-text{top:1540px;left:598px;width:492px;font-size:13.5px;line-height:21.4px;color:var(--white)}
.about-cta{top:1823px;left:598px;width:143px;height:38px;font-size:14px}

/* tools */
.feature-card{top:2102px;left:110px;width:470px;height:511px;background:var(--white);box-shadow:0 0 0 1px #e3e6e8,0 2px 6px rgba(0,0,0,.12)}
.feature-photo{height:252px}
.feature-body{padding:30px 24px}
.feature-title{font-weight:700;font-size:13.5px;line-height:23px;text-transform:uppercase;color:#222}
.meta{margin-top:14px;display:flex;gap:34px;font-size:12px;color:var(--muted);align-items:center}
.meta span{display:flex;align-items:center;gap:7px}
.feature-desc{margin-top:18px;font-size:13.5px;line-height:25px;color:var(--muted)}
.read-more{margin-top:18px;width:140px;height:46px;font-size:13px;font-weight:700}
.tip-card{left:594px;width:491px;height:157px;display:flex;background:var(--white);box-shadow:0 0 0 1px #e3e6e8,0 2px 6px rgba(0,0,0,.12)}
.tip-photo{width:241px;height:100%}
.tip-body{padding:28px 22px 0 23px}
.tip-title{font-weight:700;font-size:13.5px;line-height:23px;text-transform:uppercase;color:#222}
.tip-desc{margin-top:12px;font-size:13.5px;line-height:25px;color:var(--muted)}
.carousel-arrow{top:2980px}

/* ask */
.ask-band{top:3333px;left:0;width:1200px;height:249px;background:linear-gradient(90deg,#22b6df 0%,#27bde3 50%,#1fb0d9 100%)}
.ask-title{top:3392px;left:0;width:1200px;text-align:center;font-family:"Roboto",Arial,sans-serif;font-weight:500;font-size:31px;color:var(--white)}
.ask-input{top:3451px;left:299px;width:459px;height:54px;background:var(--white);border:none;font-family:"Arimo",Arial,sans-serif;font-size:14px;color:#555;padding-left:22px;display:flex;align-items:center}
.ask-submit{top:3451px;left:767px;width:134px;height:54px;background:var(--slate);color:var(--white);font-family:"Roboto",Arial,sans-serif;font-weight:700;font-size:15px;display:flex;align-items:center;justify-content:center}

/* footer */
.site-footer{top:3582px;left:0;width:1200px;height:372px;background:var(--footer)}
.contact-col{top:3671px;width:316px;height:187px;text-align:center;color:var(--white)}
.contact-col.highlight{background:var(--cyan)}
.contact-icon{margin:15px auto 0;width:64px;height:64px;border-radius:50%;background:var(--cyan);display:flex;align-items:center;justify-content:center}
.highlight .contact-icon{background:var(--white)}
.contact-head{margin-top:14px;font-family:"Roboto",Arial,sans-serif;font-size:18px;color:var(--white)}
.highlight .contact-head{font-weight:700;text-transform:uppercase}
.contact-line{margin-top:6px;font-size:14px;color:#b8bfc5;line-height:22px}
.contact-line.strong{font-weight:700;margin-top:2px}
.highlight .contact-line{color:var(--white);font-size:13px;line-height:23px}
.footer-rule{top:3887px;left:107px;width:978px;height:1px;background:#4b5660}
.copyright{top:3902px;left:107px;font-size:14px;color:var(--white)}
.footer-links{top:3903px;left:390px;display:flex;font-size:14px;color:var(--white)}
.footer-links a{color:var(--white);text-decoration:none;padding:0 17px;border-left:1px solid var(--white);line-height:14px}
.footer-links a:first-child{border-left:none;padding-left:0}
.footer-social{top:3896px;left:967px;display:flex;gap:4px}
.footer-social span{width:27px;height:27px;border-radius:50%;border:1.5px solid var(--white)}
</style>
</head>
<body>

<!-- header -->
<div class="abs topline"></div>
<svg class="abs nav-pointer" width="14" height="12" viewBox="0 0 14 12"><polygon points="0,0 14,0 7,12" fill="#22b6df"/></svg>
<nav class="abs main-nav">
  <a href="#">Home</a>
  <a href="#">Job Opportunities</a>
  <a href="#">Tools &amp; Career Advice</a>
  <a href="#">Ask a Job Question?</a>
  <a href="#">Volunteer Opportunities</a>
  <a href="#">About Us</a>
</nav>

<!-- hero -->
<div class="abs hero" role="img" aria-label="Photo of a smiling high school student working on a laptop"></div>
<div class="abs hero-shade"></div>
<div class="abs brand-box"><span class="brand-name">brightlarkyard.com</span></div>
<h1 class="abs hero-title">HIGHSCHOOL STUDENTS<br>START HERE</h1>
<a class="abs btn-pill hero-cta" href="#">Get Started</a>
<div class="abs hero-dots"><span></span><span class="active"></span><span></span></div>
<div class="abs hero-social" aria-label="Social links"><span></span><span></span><span></span><span></span></div>

<!-- job opportunities -->
<h2 class="section-title" style="top:791px">JOB OPPORTUNITIES</h2>
<div class="abs card-row" style="top:864px">
  <article class="listing-card" style="height:439px">
    <div class="listing-photo" role="img" aria-label="Photo of a young man working at a laptop in an office" style="background:linear-gradient(135deg,#6f7c74,#b9b3a6 55%,#5b6a70)"></div>
    <div class="listing-body">
      <h3 class="listing-title">Lorem ipsum dolor sit</h3>
      <p class="listing-company">Company Name</p>
      <p class="listing-desc">Lorem ipsum dolor sit amet, consectetur adipiscing elit, sed do eiusmod tempor incididunt ut labore et dolore magna aliqua.</p>
    </div>
    <a class="employer-btn" href="#">EMPLOYER</a>
  </article>
  <article class="listing-card" style="height:439px">
    <div class="listing-photo" role="img" aria-label="Photo of a young woman at a desk in a bright office" style="background:linear-gradient(135deg,#e6e6e4,#9aa2a6 55%,#4a5258)"></div>
    <div class="listing-body">
      <h3 class="listing-title">Lorem ipsum dolor sit</h3>
      <p class="listing-company">Company Name</p>
      <p class="listing-desc">Lorem ipsum dolor sit amet, consectetur adipiscing elit, sed do eiusmod tempor incididunt ut labore et dolore magna aliqua.</p>
    </div>
    <a class="employer-btn" href="#">EMPLOYER</a>
  </article>
  <article class="listing-card" style="height:439px">
    <div class="listing-photo" role="img" aria-label="Photo of a young man with glasses using a laptop by a window" style="background:linear-gradient(135deg,#a7b8c3,#e3e7e8 50%,#7d8f6e)"></div>
    <div class="listing-body">
      <h3 class="listing-title">Lorem ipsum dolor sit</h3>
      <p class="listing-company">Company Name</p>
      <p class="listing-desc">Lorem ipsum dolor sit amet, consectetur adipiscing elit, sed do eiusmod tempor incididunt ut labore et dolore magna aliqua.</p>
    </div>
    <a class="employer-btn" href="#">EMPLOYER</a>
  </article>
</div>

<!-- about -->
<section class="abs about-band" role="img" aria-label="Dim background photo of students in a library"></section>
<div class="abs about-art" role="img" aria-label="Illustration of a graduation owl framing a student photo"></div>
<h2 class="abs about-title">ABOUT US</h2>
<p class="abs about-text">Lorem ipsum dolor sit amet, consectetur adipiscing elit, sed do eiusmod tempor incididunt ut labore et dolore magna aliqua. Ut enim ad minim veniam, quis nostrud exercitation ullamco laboris nisi ut aliquip ex ea commodo consequat. Duis aute irure dolor in reprehenderit in voluptate velit esse cillum dolore eu fugiat nulla pariatur. Excepteur sint occaecat cupidatat non proident, sunt in culpa qui officia deserunt mollit anim id est laborum.Lorem ipsum dolor sit amet, consectetur adipiscing elit, sed do eiusmod tempor incididunt ut labore et dolore magna aliqua. Ut enim ad minim veniam, quis nostrud exercitation ullamco laboris nisi ut aliquip ex ea commodo consequat. Duis aute irure dolor in reprehenderit in voluptate velit esse cillum dolore eu fugiat nulla pariatur. Excepteur sint occaecat cupidatat non proident, sunt in culpa qui officia deserunt mollit anim id est laborum.</p>
<a class="abs btn-pill about-cta" href="#">Learn More</a>

<!-- tools & career advice -->
<h2 class="section-title" style="top:2034px">TOOLS &amp; CAREER ADVICE</h2>
<article class="abs feature-card">
  <div class="feature-photo" role="img" aria-label="Photo of a group of young colleagues talking in an office" style="background:linear-gradient(135deg,#c9d0d2,#8f8478 45%,#3f3b3a)"></div>
  <div class="feature-body">
    <h3 class="feature-title">Sed ut perspiciatis unde omnis iste natus error<br>sit voluptatem accusantium</h3>
    <div class="meta">
      <span><svg width="12" height="12" viewBox="0 0 12 12"><rect x="1" y="2" width="10" height="9" fill="none" stroke="#22b6df" stroke-width="1.3"/><line x1="1" y1="5" x2="11" y2="5" stroke="#22b6df" stroke-width="1.3"/></svg>27/02/2020</span>
      <span><svg width="12" height="12" viewBox="0 0 12 12"><circle cx="6" cy="4" r="2.5" fill="none" stroke="#22b6df" stroke-width="1.3"/><path d="M1.5 11.5c0-3 2-4.5 4.5-4.5s4.5 1.5 4.5 4.5" fill="none" stroke="#22b6df" stroke-width="1.3"/></svg>Mara Linwood</span>
      <span><svg width="13" height="12" viewBox="0 0 13 12"><ellipse cx="6.5" cy="5" rx="5.5" ry="4" fill="none" stroke="#22b6df" stroke-width="1.3"/><path d="M3 8.5 2 11.5 6 9" fill="#22b6df"/></svg>1,000</span>
    </div>
    <p class="feature-desc">Natur aut odit aut fugit, sed quia consequuntur magni dolores eos qui ratione voluptatem sequi nesciunt.</p>
    <a class="btn-pill read-more" href="#">READ MORE&nbsp;<svg width="12" height="12" viewBox="0 0 12 12"><circle cx="6" cy="6" r="6" fill="#fff"/><path d="M4 3.5 7 6 4 8.5" fill="none" stroke="#22b6df" stroke-width="1.6"/></svg></a>
  </div>
</article>
<article class="abs tip-card" style="top:2102px">
  <div class="tip-photo" role="img" aria-label="Photo of a team stacking hands together" style="background:linear-gradient(135deg,#7e8ea0,#c9a78c 50%,#3e4f63)"></div>
  <div class="tip-body"><h4 class="tip-title">Et harum quidem rerum<br>facilis est et</h4><p class="tip-desc">rnatur aut odit aut fugit, sed<br>quia consequuntur.</p></div>
</article>
<article class="abs tip-card" style="top:2279px">
  <div class="tip-photo" role="img" aria-label="Photo of a job interview across a desk" style="background:linear-gradient(135deg,#e4e8ea,#b8b1a8 50%,#6d7e8c)"></div>
  <div class="tip-body"><h4 class="tip-title">Et harum quidem rerum<br>facilis est et</h4><p class="tip-desc">rnatur aut odit aut fugit, sed<br>quia consequuntur.</p></div>
</article>
<article class="abs tip-card" style="top:2455px">
  <div class="tip-photo" role="img" aria-label="Photo of hands signing a document" style="background:linear-gradient(135deg,#4d5a66,#9aa3aa 50%,#2f3a44)"></div>
  <div class="tip-body"><h4 class="tip-title">Et harum quidem rerum<br>facilis est et</h4><p class="tip-desc">rnatur aut odit aut fugit, sed<br>quia consequuntur.</p></div>
</article>

<!-- volunteer opportunities -->
<h2 class="section-title" style="top:2706px">VOLUNTEER OPPORTUNITIES</h2>
<svg class="abs carousel-arrow" style="left:52px" width="12" height="20" viewBox="0 0 12 20"><polygon points="12,0 12,20 0,10" fill="#2e3b47"/></svg>
<svg class="abs carousel-arrow" style="left:1136px" width="12" height="20" viewBox="0 0 12 20"><polygon points="0,0 0,20 12,10" fill="#2e3b47"/></svg>
<div class="abs card-row" style="top:2779px">
  <article class="listing-card" style="height:463px">
    <div class="listing-photo" role="img" aria-label="Photo of a cheerful young woman celebrating at a laptop" style="background:linear-gradient(135deg,#d8cfc4,#f2eee9 50%,#a89a8a)"></div>
    <div class="listing-body">
      <h3 class="listing-title">Lorem ipsum dolor sit</h3>
      <p class="listing-company">Company Name</p>
      <p class="listing-desc">Lorem ipsum dolor sit amet, consectetur adipiscing elit, sed do eiusmod tempor incididunt ut labore et dolore magna aliqua.</p>
      <a class="contact-btn" href="#">CONTACT US</a>
    </div>
  </article>
  <article class="listing-card" style="height:463px">
    <div class="listing-photo" role="img" aria-label="Photo of a smiling young man at a laptop with a plant" style="background:linear-gradient(135deg,#efece6,#c7b9a4 50%,#6b6f55)"></div>
    <div class="listing-body">
      <h3 class="listing-title">Lorem ipsum dolor sit</h3>
      <p class="listing-company">Company Name</p>
      <p class="listing-desc">Lorem ipsum dolor sit amet, consectetur adipiscing elit, sed do eiusmod tempor incididunt ut labore et dolore magna aliqua.</p>
      <a class="contact-btn" href="#">CONTACT US</a>
    </div>
  </article>
  <article class="listing-card" style="height:463px">
    <div class="listing-photo" role="img" aria-label="Photo of a bearded young man typing at a laptop" style="background:linear-gradient(135deg,#e9e7e2,#a6907a 50%,#5c6a56)"></div>
    <div class="listing-body">
      <h3 class="listing-title">Lorem ipsum dolor sit</h3>
      <p class="listing-company">Company Name</p>
      <p class="listing-desc">Lorem ipsum dolor sit amet, consectetur adipiscing elit, sed do eiusmod tempor incididunt ut labore et dolore magna aliqua.</p>
      <a class="contact-btn" href="#">CONTACT US</a>
    </div>
  </article>
</div>

<!-- ask a job question -->
<section class="abs ask-band"></section>
<h2 class="abs ask-title">ASK A JOB QUESTION?</h2>
<div class="abs ask-input">Email address</div>
<div class="abs ask-submit">SUBMIT</div>

<!-- footer -->
<footer class="abs site-footer"></footer>
<div class="abs contact-col" style="left:112px">
  <div class="contact-icon"><svg width="30" height="30" viewBox="0 0 24 24"><path d="M6.6 10.8c1.4 2.8 3.8 5.1 6.6 6.6l2.2-2.2c.3-.3.7-.4 1-.2 1.1.4 2.3.6 3.6.6.6 0 1 .4 1 1V20c0 .6-.4 1-1 1C10.6 21 3 13.4 3 4c0-.6.4-1 1-1h3.5c.6 0 1 .4 1 1 0 1.3.2 2.5.6 3.6.1.3 0 .7-.2 1l-2.3 2.2z" fill="#fff"/></svg></div>
  <p class="contact-head">Call Us Now</p>
  <p class="contact-line">Office Telephone :</p>
  <p class="contact-line strong">+1 888 888 8888</p>
</div>
<div class="abs contact-col highlight" style="left:442px">
  <div class="contact-icon"><svg width="28" height="34" viewBox="0 0 24 30"><path d="M12 2C7 2 3.5 5.6 3.5 10.3 3.5 16.5 12 27 12 27s8.5-10.5 8.5-16.7C20.5 5.6 17 2 12 2z" fill="none" stroke="#22b6df" stroke-width="2"/><circle cx="12" cy="10.3" r="3.2" fill="none" stroke="#22b6df" stroke-width="2"/></svg></div>
  <p class="contact-head">Come Visit Us</p>
  <p class="contact-line">123,Lorem ipsum dolor sit amet,<br>consectetur adipiscing</p>
</div>
<div class="abs contact-col" style="left:772px">
  <div class="contact-icon"><svg width="30" height="24" viewBox="0 0 30 24"><rect x="2" y="3" width="26" height="18" rx="2" fill="#fff"/><path d="M3 5l12 9 12-9" fill="none" stroke="#22b6df" stroke-width="2"/></svg></div>
  <p class="contact-head">Send Us A Message</p>
  <p class="contact-line strong" style="margin-top:6px">Main Email : info@companyname.com</p>
  <p class="contact-line strong">Internet : www.website-address.com</p>
</div>
<div class="abs footer-rule"></div>
<p class="abs copyright">© 2021. Company name</p>
<nav class="abs footer-links"><a href="#">About</a><a href="#">Blog</a><a href="#">Privacy policy</a><a href="#">Terms</a><a href="#">Contact</a></nav>
<div class="abs footer-social" aria-label="Social links"><span></span><span></span><span></span><span></span></div>

</body>
</html>
```